Lanterns in Winter

A 3rd Volume of Poetry, dealing with Power, Politics, Love, and General topics. The major theme is the misuse of power across al the continents. I would like a background map of the world and a stylistic fire depicting symbolically each continent on fire. This can be abstract. The title may be included in the artwork. alone or in conjunction with the world map.

```html
<!DOCTYPE html>
<html lang="en">
<head>
<meta charset="UTF-8">
<title>Lanterns in Winter – Book Cover</title>
<link href="https://fonts.googleapis.com/css2?family=Rubik+Wet+Paint&family=Domine:wght@700&family=Cinzel:wght@400&family=Arimo:wght@400&display=swap" rel="stylesheet">
<style>
  :root {
    --page: #ffffff;
    --cover-black: #0d0d0d;
    --title-yellow: #f2c21c;
    --author-white: #ffffff;
    --panel-rust: rgba(150, 58, 12, 0.88);
    --panel-gold: #dba52a;
    --body-text: #f3e6dc;
    --map-glow: #f0a81c;
    --fire-deep: #b83a06;
    --fire-bright: #ffb21e;
  }
  * { margin: 0; padding: 0; box-sizing: border-box; }
  html, body {
    width: 1200px; height: 850px; overflow: hidden;
    background: var(--page);
  }
  .stage {
    position: relative; width: 1200px; height: 850px;
    display: flex; justify-content: center; align-items: center; gap: 40px;
  }
  .cover {
    position: relative; width: 340px; height: 500px;
    background: var(--cover-black); overflow: hidden;
  }

  /* Front cover */
  .front-title {
    position: absolute; top: 18px; left: 0; right: 0;
    text-align: center;
    font-family: "Rubik Wet Paint", cursive;
    font-size: 54px; line-height: 1.02; color: var(--title-yellow);
    text-transform: uppercase; letter-spacing: 1px;
  }
  .front-author {
    position: absolute; top: 152px; left: 0; right: 0; text-align: center;
    font-family: "Domine", serif; font-weight: 700;
    font-size: 17px; color: var(--author-white);
  }
  .world-map {
    position: absolute; left: 10px; top: 190px; width: 300px; height: 220px;
    background: radial-gradient(ellipse at 50% 45%, rgba(240,168,28,0.35), rgba(240,168,28,0.08) 60%, transparent 75%);
  }
  .fire {
    position: absolute; left: 0; right: 0; bottom: 0; height: 130px;
    background: linear-gradient(to top, var(--fire-deep) 0%, #e2650f 35%, var(--fire-bright) 60%, rgba(255,178,30,0) 100%);
  }

  /* Back cover */
  .back-map {
    position: absolute; right: 0; top: 270px; width: 40px; height: 160px;
    background: linear-gradient(to bottom, rgba(240,168,28,0.05), rgba(240,168,28,0.35), rgba(240,168,28,0.05));
  }
  .back-panel {
    position: absolute; left: 10px; top: 48px; width: 306px; height: 410px;
    background: var(--panel-rust); padding: 6px 12px 0;
  }
  .back-title {
    font-family: "Cinzel", serif; font-weight: 400;
    font-size: 38px; line-height: 1.02; color: var(--panel-gold);
    text-transform: uppercase;
  }
  .back-author {
    margin-top: 6px;
    font-family: "Domine", serif; font-weight: 700;
    font-size: 15px; color: var(--panel-gold);
  }
  .back-blurb {
    margin-top: 10px;
    font-family: "Arimo", sans-serif;
    font-size: 13px; line-height: 1.62; color: var(--body-text);
  }
</style>
</head>
<body>
  <main class="stage">
    <section class="cover cover-front">
      <h1 class="front-title">Lanterns<br>in Winter</h1>
      <p class="front-author">Harlan T Voss</p>
      <div class="world-map" role="img" aria-label="Glowing orange outline map of the world's continents"></div>
      <div class="fire" role="img" aria-label="Stylised flames rising along the bottom edge"></div>
    </section>

    <section class="cover cover-back">
      <div class="back-map" role="img" aria-label="Edge of the glowing world map wrapping from the spine"></div>
      <div class="fire" role="img" aria-label="Stylised flames rising along the bottom edge"></div>
      <div class="back-panel">
        <h2 class="back-title">Lanterns<br>in Winter</h2>
        <p class="back-author">Harlan T Voss</p>
        <p class="back-blurb">In this third collection of poems, the poet turns a steady gaze on power and the people who hold it. From crowded capitals to quiet villages, these verses follow rulers and the ruled, promises made and broken, and the small acts of courage that answer them. Alongside the politics run poems of love, memory and ordinary days, each one a lantern lit against a long winter. Sharp, tender and restless, the book asks what we owe one another when the world seems to burn on every shore.</p>
      </div>
    </section>
  </main>
</body>
</html>
```